Business card design needed for Renewable utilities company based in New Zealand.

We supply and install solar panels and all components along with it for a fully customisable PV system that helps customer save money on their energy bills right away and also save the planet!

I have attached logo & website design files to give you a better insight.

Business

```html
<!DOCTYPE html>
<html lang="en">
<head>
<meta charset="utf-8">
<title>Sunward Grid — Business Card</title>
<link rel="stylesheet" href="https://fonts.googleapis.com/css2?family=Open+Sans:wght@400;600&display=swap">
<style>
  :root {
    --bg: #e4e4e6;
    --card-white: #f7f7f8;
    --card-grey: #e9e9ec;
    --navy: #1d2f66;
    --navy-deep: #17275a;
    --navy-light: #43679b;
    --band: #2e4791;
    --accent: #29a3e0;
    --ink-light: #ffffff;
    --ink-soft: #dfe6f3;
  }
  * { margin: 0; padding: 0; box-sizing: border-box; }
  html, body {
    width: 1200px; height: 1000px; overflow: hidden;
    background: var(--bg);
    font-family: "Open Sans", Arial, sans-serif;
  }
  .canvas { position: relative; width: 1200px; height: 1000px; }

  .card {
    position: absolute;
    width: 560px; height: 320px;
    border-radius: 28px;
    overflow: hidden;
    box-shadow: 0 6px 18px rgba(0,0,0,0.18);
  }

  /* Front */
  .card-front {
    left: 90px; top: 120px;
    background: linear-gradient(135deg, var(--card-white) 0%, var(--card-grey) 100%);
  }
  .card-front .facets { position: absolute; inset: 0; }
  .front-stripe {
    position: absolute; left: 0; right: 0; top: 70px; height: 10px;
    background: var(--band);
  }
  .front-brand {
    position: absolute; left: 0; right: 0; top: 100px;
    display: flex; flex-direction: column; align-items: center; gap: 14px;
  }
  .brand-dot {
    width: 78px; height: 78px; border-radius: 50%;
    background: var(--navy);
  }
  .card-front .brand-name {
    font-size: 38px; font-weight: 400; color: var(--navy); letter-spacing: 0.5px;
  }
  .tagline-band {
    position: absolute; left: 0; right: 0; bottom: 32px; height: 34px;
    background: var(--band);
    display: flex; align-items: center; justify-content: center;
  }
  .tagline {
    color: var(--ink-light); font-size: 17px; font-weight: 600; letter-spacing: 0.3px;
  }

  /* Back */
  .card-back {
    left: 560px; top: 520px;
    background: radial-gradient(circle at 22% 15%, var(--navy-light) 0%, var(--navy) 55%, var(--navy-deep) 100%);
    color: var(--ink-soft);
  }
  .card-back .facets { position: absolute; inset: 0; }
  .back-brand {
    position: absolute; left: 40px; top: 110px;
    display: flex; flex-direction: column; align-items: flex-start; gap: 14px;
  }
  .back-brand .brand-dot { background: var(--ink-light); margin-left: 40px; }
  .card-back .brand-name {
    font-size: 30px; font-weight: 400; color: var(--ink-light); letter-spacing: 0.5px;
  }
  .contact {
    position: absolute; left: 320px; top: 44px;
    font-size: 14px; line-height: 1.35;
  }
  .contact .person { font-size: 19px; color: var(--ink-light); }
  .contact .person .surname { color: var(--accent); }
  .contact .role { font-size: 13px; margin-bottom: 18px; }
  .contact .address { margin-bottom: 16px; }
  .contact-line { display: flex; align-items: center; gap: 7px; }
  .contact-line svg { width: 14px; height: 14px; fill: var(--ink-light); }
  .contact .web { padding-left: 21px; }
</style>
</head>
<body>
<main class="canvas">

  <section class="card card-front" aria-label="Card front">
    <svg class="facets" viewBox="0 0 560 320" preserveAspectRatio="none" aria-hidden="true">
      <polygon points="0,0 220,0 90,320 0,320" fill="#ffffff" opacity="0.5"/>
      <polygon points="300,0 560,0 560,200" fill="#dcdce0" opacity="0.35"/>
      <polygon points="160,320 420,90 520,320" fill="#ffffff" opacity="0.35"/>
    </svg>
    <div class="front-stripe"></div>
    <div class="front-brand">
      <div class="brand-dot"></div>
      <div class="brand-name">Sunward Grid</div>
    </div>
    <div class="tagline-band">
      <p class="tagline">The Best Solar Energy Specialists in Australia!</p>
    </div>
  </section>

  <section class="card card-back" aria-label="Card back">
    <svg class="facets" viewBox="0 0 560 320" preserveAspectRatio="none" aria-hidden="true">
      <polygon points="0,320 180,0 300,0 120,320" fill="#ffffff" opacity="0.04"/>
      <polygon points="340,320 560,60 560,320" fill="#000000" opacity="0.08"/>
    </svg>
    <div class="back-brand">
      <div class="brand-dot"></div>
      <div class="brand-name">Sunward Grid</div>
    </div>
    <div class="contact">
      <p class="person">Alex <span class="surname">Marlow</span></p>
      <p class="role">Director</p>
      <p class="address">48 Harbour View Road<br>Wellington 6011<br>PO Box 512</p>
      <p class="contact-line">
        <svg viewBox="0 0 24 24" aria-hidden="true"><path d="M6.6 10.8a15 15 0 0 0 6.6 6.6l2.2-2.2a1 1 0 0 1 1-.25 11.4 11.4 0 0 0 3.6.57 1 1 0 0 1 1 1V20a1 1 0 0 1-1 1A17 17 0 0 1 3 4a1 1 0 0 1 1-1h3.5a1 1 0 0 1 1 1c0 1.25.2 2.45.57 3.57a1 1 0 0 1-.25 1z"/></svg>
        0800-555-0192
      </p>
      <p class="contact-line">
        <svg viewBox="0 0 24 24" aria-hidden="true"><path d="M2 5h20v14H2zm2 2v.5l8 5 8-5V7l-8 5z"/></svg>
        a.marlow@sunwardgrid.com
      </p>
      <p class="web">www.sunwardgrid.com</p>
    </div>
  </section>

</main>
</body>
</html>
```